Software Company Banner Ad

We need a banner ad in two sizes. 728x90 and 300x250.
They should have strong similarity to the following ads:
http://www.vexlo.net/search/results?brand[0]=quorp&ad=4821396
http://www.vexlo.net/search/results?brand[0]=dravensoft&ad=4830517
Idea will be very similar. We want the same grey color, white text, and a realistic owl that blinks. The owl should have dramatic, bright, yellow eyes. The text will animate "from the top" as in the example. Though the logo animation will be different, all text and non-logo animation should match the animation in the example advertisements. The text will rotate between the following four sentences and images.
Looking for a provider of procurement cloud apps?
[Images - attached below]
The experts really liked our KTV booth.
Get great results with every procurement. [Learn more]
There are three vector files attached below. Feel free to change the colors as necessary to match the color scheme of the ad. We need one 2013 and one 2014 award in the ad.
The awards could appear simultaneously, could swap with each other or could appear in succession. Animation is acceptable.
There is an additional vector file with the company logo. The company logo should go where the Quorp logo is in horizontal ad. The company logo should go where the Dravensoft logo is in the block ad. The example ad has two logos. We will only need one logo on our ads. The logo should be changed to the color of the text used for the ad (white).
The owls eyes should slowly blink two times (as in the example).
The owl eyes should immediately grab someone's attention and all colors should compliment these eyes.
The [Learn more] button should have animation. The button should match the color of the owl's eyes. There should be a line/gleam/glare of light that travels across the button. The button should be embossed with the subtle animation occurring each time it appears.
Ads should be done with flash. We will need the source files and the names of any fonts used at the end of the project.
Thank you and please do not hesitate to contact with any questions.
Reason: We have contacted several photographers to see if the alternative owl images are available on Pixvane, Framelodge or similar. The duration extension is to accommodate this.
Target Market(s)
Target customers are procurement department employees of large companies.
Industry/Entity Type
It Company

```html
<!DOCTYPE html>
<html lang="en">
<head>
<meta charset="utf-8">
<title>Orvane – Procurement Cloud Apps Banner</title>
<link rel="stylesheet" href="https://fonts.googleapis.com/css2?family=Oswald:wght@500;600;700&display=swap">
<style>
  :root {
    --grey-light: #a2a2a2;
    --grey-mid: #858585;
    --grey-dark: #5e5e5e;
    --grey-deep: #4c4c4c;
    --text-white: #ffffff;
    --owl-dark: #3a3128;
    --owl-brown: #6b5c4a;
    --owl-tan: #9c8b74;
    --owl-yellow: #e6f020;
    --owl-yellow-soft: #c9cf4a;
  }
  * { margin: 0; padding: 0; box-sizing: border-box; }
  html, body { width: 1200px; height: 148px; overflow: hidden; background: var(--grey-mid); }
  .banner {
    position: relative;
    width: 1200px;
    height: 148px;
    overflow: hidden;
    background: linear-gradient(90deg, var(--grey-light) 0%, var(--grey-mid) 30%, var(--grey-dark) 62%, var(--grey-deep) 100%);
    font-family: "Oswald", "Arial Narrow", sans-serif;
    color: var(--text-white);
  }
  .banner__facet {
    position: absolute;
    inset: 0;
    width: 1200px;
    height: 148px;
  }
  .brand {
    position: absolute;
    left: 14px;
    top: 7px;
    font-weight: 700;
    font-size: 31px;
    letter-spacing: 1px;
    line-height: 1;
    text-transform: uppercase;
    color: var(--text-white);
  }
  .headline {
    position: absolute;
    left: 234px;
    width: 406px;
    top: 27px;
    font-weight: 500;
    font-size: 30px;
    line-height: 38px;
    letter-spacing: 0.4px;
    text-transform: uppercase;
    text-align: center;
    color: var(--text-white);
  }
  .owl-photo {
    position: absolute;
    right: 0;
    top: 0;
    width: 440px;
    height: 148px;
    background:
      radial-gradient(ellipse 190px 42px at 62% 44%, var(--owl-yellow) 0%, var(--owl-yellow-soft) 35%, rgba(156,139,116,0) 100%),
      radial-gradient(ellipse 220px 120px at 62% 60%, var(--owl-tan) 0%, var(--owl-brown) 55%, rgba(107,92,74,0) 100%),
      linear-gradient(90deg, rgba(58,49,40,0) 0%, var(--owl-dark) 22%, var(--owl-brown) 60%, var(--owl-dark) 100%);
  }
</style>
</head>
<body>
  <div class="banner">
    <svg class="banner__facet" viewBox="0 0 1200 148" aria-hidden="true">
      <polygon points="0,0 160,0 0,148" fill="#ffffff" opacity="0.10"/>
      <polygon points="0,70 85,148 0,148" fill="#000000" opacity="0.07"/>
    </svg>

    <div class="brand">Orvane</div>

    <h1 class="headline">Looking for a provider of<br>procurement cloud apps?</h1>

    <div class="owl-photo" role="img" aria-label="Close-up photo of a great horned owl with dramatic bright yellow eyes"></div>
  </div>
</body>
</html>
```